Eye-catching & Glamorous Labels for Skincare Bottles & Jars

We need new labels designed for our product range as we have been dormant for a few years and are now rebranding Velora Grace - Kindly Made Skincare. The label sizes are defined in the attached word document. All products have either a bright silver or a matte silver lid pump/spray so please keep this in mind.

We are open to colours and invite you to create bright trendy labels which are coordinated with the logo attached. The logo is not of any specific colour so dark on light, light on dark, tone on tone - we like purple / duck egg blue / turquoise WITH matte silver, however stronger colours like navy plus maroon with matte silver is also a strong favourite. If you feel inspired by a colour you think would be appropriate to Velora Grace please feel free to have a go.

A front section for product information is required and the back should include relevant details ie ingredients, company info, and a note that there has been no testing on animals.

The serum bottle will require a front and back label on a clear label in a pale colour to coordinate with the rest of the range. Size for this label is 35mm top edge, 25mm bottom edge, height 45mm - I have attached a picture of the serum bottle as they were originally pad printed. Please don't hesitate to contact me for any further information. Good luck!

Target Market(s)

Educated professional women 30-45 who are regular skincare users and looking for beautiful skincare products without animal derived ingredients and animal testing

Industry/Entity Type

Skin Care Product

Font styles to use
Serif
Sans Serif
Decorative
Script

Colors

Designer to choose colors to be used in the design.

Requirements
Must have
• Velora Grace Logo - eye catching design - not too busy or cramped.
Nice to have
• Is it possible to create a background pattern using a very small image of the logo? Just a thought.

```html
<!DOCTYPE html>
<html lang="en">
<head>
<meta charset="utf-8">
<title>Velora Grace – Oil Serum Labels</title>
<link rel="stylesheet" href="https://fonts.googleapis.com/css2?family=Archivo+Black&family=Crimson+Text:wght@400;600;700&display=swap">
<style>
  :root {
    --page: #ffffff;
    --ink: #ffffff;
    --shade-top: #2a2627;
    --shade-upper: #4c4440;
    --shade-mid: #6a5048;
    --shade-low: #773f3a;
    --shade-bottom: #7a2e35;
    --serif: "Crimson Text", Georgia, serif;
    --display: "Archivo Black", "Arial Black", sans-serif;
  }
  * { box-sizing: border-box; margin: 0; padding: 0; }
  html, body {
    width: 1200px; height: 1200px; overflow: hidden;
    background: var(--page);
  }
  .sheet { position: relative; width: 1200px; height: 1200px; }

  .label {
    position: absolute;
    color: var(--ink);
    background: linear-gradient(to bottom,
      var(--shade-top) 0%, var(--shade-upper) 25%,
      var(--shade-mid) 55%, var(--shade-low) 80%, var(--shade-bottom) 100%);
  }
  .label > * {
    position: absolute; left: 0; right: 0;
    text-align: center; white-space: nowrap; line-height: 1;
  }

  .brand-name {
    font-family: var(--serif); font-weight: 600;
    font-size: var(--name-size); letter-spacing: 0.02em;
  }
  .brand-tagline {
    font-family: var(--serif); font-weight: 400;
    font-size: var(--tag-size); letter-spacing: 0.34em;
  }
  .product-range {
    font-family: var(--serif); font-weight: 600;
    font-size: var(--range-size);
  }
  .product-name {
    font-family: var(--display);
    font-size: var(--product-size); letter-spacing: 0.04em;
  }
  .product-note {
    font-family: var(--serif); font-weight: 700;
    font-size: var(--note-size); letter-spacing: 0.28em;
  }
  .product-volume {
    font-family: var(--serif); font-weight: 600;
    font-size: var(--volume-size);
  }

  /* tall bottle label, left */
  .label--tall {
    left: 218px; top: 45px; width: 264px; height: 827px;
    --name-size: 38px; --tag-size: 12px; --range-size: 22px;
    --product-size: 36px; --note-size: 15px; --volume-size: 15px;
  }
  .label--tall .brand-name { top: 331px; }
  .label--tall .brand-tagline { top: 367px; }
  .label--tall .product-range { top: 528px; }
  .label--tall .product-name { top: 560px; }
  .label--tall .product-note { top: 600px; }
  .label--tall .product-volume { top: 665px; }

  /* large bottle label, right */
  .label--large {
    left: 701px; top: 37px; width: 346px; height: 946px;
    --name-size: 50px; --tag-size: 16px; --range-size: 28px;
    --product-size: 46px; --note-size: 19px; --volume-size: 19px;
  }
  .label--large .brand-name { top: 365px; }
  .label--large .brand-tagline { top: 411px; }
  .label--large .product-range { top: 617px; }
  .label--large .product-name { top: 657px; }
  .label--large .product-note { top: 706px; }
  .label--large .product-volume { top: 790px; }

  /* wide jar label, bottom */
  .label--wide {
    left: 185px; top: 909px; width: 473px; height: 260px;
    --name-size: 34px; --tag-size: 10.5px; --range-size: 18px;
    --product-size: 29px; --note-size: 13px; --volume-size: 13px;
  }
  .label--wide .brand-name,
  .label--wide .brand-tagline { left: 20px; right: auto; width: 218px; }
  .label--wide .product-range,
  .label--wide .product-name,
  .label--wide .product-note,
  .label--wide .product-volume { left: 250px; right: auto; width: 210px; }
  .label--wide .brand-name { top: 156px; }
  .label--wide .brand-tagline { top: 184px; }
  .label--wide .product-range { top: 94px; }
  .label--wide .product-name { top: 121px; }
  .label--wide .product-note { top: 153px; }
  .label--wide .product-volume { top: 208px; }
</style>
</head>
<body>
<main class="sheet">

  <section class="label label--tall" aria-label="Tall bottle label">
    <p class="brand-name">Velora Grace</p>
    <p class="brand-tagline">KINDLY MADE SKINCARE</p>
    <p class="product-range">Youth Renewal Ritual</p>
    <h2 class="product-name">Oil Serum</h2>
    <p class="product-note">Velvet Radiance</p>
    <p class="product-volume">30ml</p>
  </section>

  <section class="label label--large" aria-label="Large bottle label">
    <p class="brand-name">Velora Grace</p>
    <p class="brand-tagline">KINDLY MADE SKINCARE</p>
    <p class="product-range">Youth Renewal Ritual</p>
    <h2 class="product-name">Oil Serum</h2>
    <p class="product-note">Velvet Radiance</p>
    <p class="product-volume">30ml</p>
  </section>

  <section class="label label--wide" aria-label="Wide jar label">
    <p class="brand-name">Velora Grace</p>
    <p class="brand-tagline">KINDLY MADE SKINCARE</p>
    <p class="product-range">Youth Renewal Ritual</p>
    <h2 class="product-name">Oil Serum</h2>
    <p class="product-note">Velvet Radiance</p>
    <p class="product-volume">30ml</p>
  </section>

</main>
</body>
</html>
```